Poster Design For Obstacle Run

Design a poster for the Crow Ridge Obstacle run.
Text: Crow Ridge Obstacle Run. May 12th, 2018. Sittard. www.crowridgedash.nl. I have added a lot of pictures.
Furthermore, the logo should be included. As an example I included a poster from the ironbark race that we really like (ironbark team challenge) and also. Feel free to take a look at our website for inspiration: www.crowridgedash.nl

```html
<!DOCTYPE html>
<html lang="en">
<head>
<meta charset="utf-8">
<title>Crow Ridge Obstacle Run</title>
<link href="https://fonts.googleapis.com/css2?family=Oswald:wght@300;400;500;600;700&display=swap" rel="stylesheet">
<style>
  :root {
    --orange: #ee6a2a;
    --white: #ffffff;
    --mud-dark: #3a2c18;
    --mud-mid: #8a6428;
    --splash: #f0a22e;
    --splash-light: #f7c35a;
    --water: #cdbf98;
    --leaf: #5a6226;
    --shirt: #f0522a;
  }
  * { margin: 0; padding: 0; box-sizing: border-box; }
  html, body { width: 849px; height: 1200px; overflow: hidden; background: var(--mud-dark); }
  .poster {
    position: relative;
    width: 849px;
    height: 1200px;
    overflow: hidden;
    font-family: "Oswald", sans-serif;
    color: var(--white);
    text-align: center;
  }
  .poster__photo {
    position: absolute;
    inset: 0;
    background:
      radial-gradient(ellipse 330px 210px at 230px 560px, rgba(240,82,42,1) 0%, rgba(240,82,42,0.85) 45%, rgba(240,82,42,0) 80%),
      radial-gradient(ellipse 520px 260px at 500px 760px, rgba(247,195,90,0.95) 0%, rgba(240,162,46,0.8) 45%, rgba(240,162,46,0) 80%),
      radial-gradient(ellipse 340px 220px at 520px 360px, rgba(205,191,152,0.9) 0%, rgba(205,191,152,0) 75%),
      radial-gradient(ellipse 240px 380px at 790px 420px, rgba(90,98,38,0.95) 0%, rgba(90,98,38,0) 75%),
      radial-gradient(ellipse 220px 260px at 330px 330px, rgba(150,100,60,0.9) 0%, rgba(150,100,60,0) 75%),
      linear-gradient(155deg, #4a4020 0%, #7c6a3c 25%, #a5782e 50%, #c88a2c 65%, #8a6428 80%, #3a2c18 100%);
  }
  .poster__shade {
    position: absolute;
    inset: 0;
    background: linear-gradient(180deg, rgba(40,30,15,0.3) 0%, rgba(40,30,15,0) 25%, rgba(40,30,15,0) 62%, rgba(30,22,10,0.6) 100%);
  }
  .title {
    position: absolute;
    top: 36px;
    left: 0;
    width: 100%;
  }
  .title__name {
    font-weight: 400;
    font-size: 152px;
    line-height: 1.1;
    color: var(--orange);
    letter-spacing: 2px;
    white-space: nowrap;
  }
  .title__event {
    margin-top: 2px;
    font-weight: 300;
    font-size: 62px;
    line-height: 1;
    letter-spacing: 26px;
    padding-left: 26px;
    white-space: nowrap;
  }
  .details {
    position: absolute;
    top: 818px;
    left: 0;
    width: 100%;
  }
  .details__date {
    font-weight: 600;
    font-size: 136px;
    line-height: 1.1;
    letter-spacing: -1px;
    white-space: nowrap;
  }
  .details__date sup {
    font-size: 62px;
    vertical-align: 54px;
    line-height: 0;
  }
  .details__place {
    font-weight: 600;
    font-size: 54px;
    line-height: 1;
    margin-top: 2px;
  }
  .details__web {
    margin-top: 66px;
    font-weight: 600;
    font-size: 54px;
    line-height: 1;
    color: var(--orange);
    letter-spacing: 1px;
  }
</style>
</head>
<body>
  <main class="poster">
    <div class="poster__photo" role="img" aria-label="Action photo of a runner in an orange shirt plunging through a muddy water obstacle, golden mud spraying across the frame"></div>
    <div class="poster__shade"></div>

    <header class="title">
      <h1 class="title__name">CROW RIDGE</h1>
      <p class="title__event">OBSTACLE RUN</p>
    </header>

    <section class="details">
      <p class="details__date">MAY 12<sup>th</sup> 2018</p>
      <p class="details__place">SITTARD</p>
      <p class="details__web">WWW.CROWRIDGEDASH.NL</p>
    </section>
  </main>
</body>
</html>
```